依頼詳細
<現状サイトの課題>
①一目で、何をしている会社なのかが分からない。
⇒商品画像・作業画像などを入れ、分かりやすく目を引き付けるようにする。

②項目が小さく、引き付けにくいデザイン。
⇒アイコンを大きくして、デザイン性を持たせる。

③自社の強みを視覚化できていない。
⇒図や写真を追加し、視覚的に伝わるようにする。

④自社の新着情報がないので社内の動きが把握できない。
⇒新着ニュースを追加し社内の動きが把握できるようにする。

⑤企業規模が小さく感じてしまう。
⇒洗練されたデザイン、コンテンツの充実、グローバルサイトの作成により企業規模をワンランク大きく見えるように表現する。
----------------------------------
<現在のサイト>
明確なサイトの情報共有はできませんが、TOPページの情報を一部伏せて共有します。添付の”TOPページ”をご参照ください。

<サイトリニューアルの方針>
①強みを明確にする為、全体的に画像化し打ち出したい。TOPページは動画を掲載し、よりリアルにユーザー様にイメージが伝わるデザインにする。

②企業規模をワンランク大きく見えるように表現し、グローバル化についてもアピールすることで、事業規模の大きい信頼出来る会社であることが分かるようにし、新規顧客の獲得および定着するようにサイトリニューアルを行う。

③必須機能
・TOPページへ動画を埋め込む。
・スマホ対応(レスポンシブウェブデザイン)にする。
・ウェブ見積り機能を設け、いつでも見積りが確認できるようにする。(TOPページにバナーを設けるなどデザインする)

<イメージ参考サイト>
①メインカラーをブルーとし、TOPページを開くとすぐに大きな画像イメージが見えます。
https://www.e-hariwa.co.jp/

②トップページに表示される、動画イメージです。
https://www.dovel.co.jp/

③コンテンツの配置や施工事例が見やすいです。
http://www.tasemi-kk.com/

④TOPページに施工写真や文字が挿入されており分かりやすい。また企業イメージがよく考えられており、ブランディングされています。
http://www.fujiyaga.co.jp/

<カラーテーマ>
①青系(堅実・信頼・クール)または水色系(さわやか・清潔感)

②青4割、白6割の配色のイメージでお願いします。制作の際は、カラーチャート(カラーを選んだ理由)もご提示いただけると幸いです。

<重視する点/検討基準>
①サイトコンセプトにあったデザイン(ご提案の際は、制作頂いたデザインコンセプト及びデザイン説明コメントの記載をお願い致します)

②納期厳守

<具体的な制作数>
TOPページ:1ページ(PC版のデザイン制作をお願いします)

<選考の進め方>
ご提案頂いたデザイン内容・コンセプトなどをもとに、プロジェクトメンバーで選考、決定致します。
※今回は、トップページデザインのみの見積りとなります。
今後、コーディングを依頼する可能性もございます。その場合は改めてクリエタスを通じてご依頼させて頂きます。パララックスデザインでのコーディングも条件として入れてまいります。
1ページ
青系、水色系
• イラストレーター形式 (.ai)
• フォトショップ形式 (.psd)
追記です。
サイトコンセプトの資料も添付いたします。
宜しくお願いいたします。

クライアント様と協議させていただき、コンセプトに合った総合的なデザインを評価させて頂きました。
その中で、クライアント様からの評価が多かった「Pixfern様」を当選とさせていただきました。ありがとうございました。

ランサーの皆さん、このように沢山の素敵なデザインをご提案頂き本当にありがとうございました。
コンセプトを基に、クライアント様とも大いに悩んで決定させて頂きました。
また、選定が期限間近になってしまいましたこと、申し訳ございませんでした。

機会があれば、今後ともどうぞ宜しくお願い致します。

```html
<!DOCTYPE html>
<html lang="ja">
<head>
<meta charset="utf-8">
<title>TOMASEI</title>
<link rel="stylesheet" href="https://fonts.googleapis.com/css2?family=Noto+Sans+JP:wght@400;500;700&family=Roboto:wght@400;500;700&display=swap">
<style>
:root{
  --navy:#15245a;
  --navy-deep:#0f1b45;
  --blue:#2a6fc0;
  --sky:#e8f1fa;
  --grey:#f3f4f6;
  --line:#dcdfe5;
  --text:#333a45;
  --muted:#7a828e;
  --white:#fff;
}
*{margin:0;padding:0;box-sizing:border-box}
html,body{width:1200px;height:2452px;overflow:hidden;background:var(--white)}
body{position:relative;font-family:"Noto Sans JP",sans-serif;color:var(--text);font-size:13px}
.abs{position:absolute}
ul{list-style:none}

/* header */
.site-header{left:0;top:0;width:1200px;height:88px;background:var(--white);border-bottom:1px solid var(--line)}
.brand{left:205px;top:20px;display:flex;align-items:center;gap:8px}
.brand-mark{width:14px;height:14px;background:var(--blue)}
.brand-name{font-family:"Roboto",sans-serif;font-weight:700;font-size:24px;color:var(--navy);letter-spacing:1px}
.brand-sub{left:227px;top:52px;font-size:11px;color:var(--navy)}
.global-nav{left:520px;top:0;height:88px;display:flex}
.global-nav li{width:66px;height:88px;border-left:1px solid var(--line);display:flex;flex-direction:column;align-items:center;justify-content:center;gap:8px;font-size:11px;color:var(--navy)}
.global-nav li::before{content:"";width:16px;height:16px;border:2px solid var(--navy);border-radius:3px}
.nav-estimate{left:984px;top:0;width:96px;height:88px;background:var(--navy);color:var(--white);font-size:11px;display:flex;align-items:center;justify-content:center;text-align:center;line-height:1.6}

/* hero */
.hero{left:0;top:88px;width:1200px;height:392px;background:
  radial-gradient(ellipse at 75% 55%,rgba(90,130,190,.45),transparent 55%),
  radial-gradient(ellipse at 20% 30%,rgba(70,100,160,.35),transparent 50%),
  linear-gradient(180deg,#2b3f6e,#15274e 70%,#1c2e58)}
.hero-title{left:0;top:190px;width:1200px;text-align:center;font-family:"Roboto",sans-serif;font-weight:500;font-size:50px;color:var(--white)}
.hero-lead{left:0;top:262px;width:1200px;text-align:center;font-size:15px;color:var(--white);letter-spacing:1px}

.features{left:0;top:480px;width:1200px;height:208px;display:flex}
.feature{flex:1;position:relative;display:flex;align-items:center;justify-content:center;text-align:center;color:var(--white);font-size:19px;line-height:1.6;font-weight:500}
.feature:nth-child(1){background:linear-gradient(135deg,#1d2a4f,#2c3c66)}
.feature:nth-child(2){background:linear-gradient(135deg,#3f86c9,#5b9ad4)}
.feature:nth-child(3){background:linear-gradient(135deg,#2c3440,#434c5a)}
.feature .arrow{position:absolute;left:50%;bottom:24px;margin-left:-15px;width:30px;height:30px}

/* works */
.section-label{left:0;width:1200px;text-align:center}
.section-label small{display:block;font-family:"Roboto",sans-serif;font-size:11px;color:var(--muted);letter-spacing:1px}
.section-label h2{font-size:20px;font-weight:500;color:var(--navy);margin-top:2px}
.works-grid{left:200px;top:770px;width:800px;display:grid;grid-template-columns:repeat(4,1fr);gap:12px}
.work{height:166px}
.btn-more{left:500px;top:1124px;width:200px;height:34px;border-radius:17px;background:var(--navy);color:var(--white);font-size:12px;display:flex;align-items:center;justify-content:center}

/* strength */
.strength{left:0;top:1200px;width:1200px;height:318px;background:var(--sky)}
.strength-photo{left:0;top:1200px;width:520px;height:318px;background:linear-gradient(135deg,#9fc1e3,#c9dff2 45%,#f4f8fc)}
.strength-body{left:540px;top:1228px;width:460px}
.strength-body h3{font-size:18px;font-weight:700;color:var(--navy);margin-bottom:18px}
.strength-body p{font-size:12px;line-height:2;color:var(--text)}
.strength-points{margin-top:16px}
.strength-points li{font-size:12px;color:var(--navy);line-height:2;display:flex;align-items:center;gap:8px}
.strength-points li::before{content:"";width:10px;height:10px;border-radius:50%;background:var(--blue)}

/* main columns */
.col-title{font-size:14px;font-weight:700;color:var(--navy);border-bottom:2px solid var(--navy);padding-bottom:6px}
.voices{left:200px;top:1562px;width:590px}
.voice-list{display:flex;gap:12px;margin-top:12px}
.voice{flex:1}
.voice-photo{height:108px}
.voice p{font-size:11px;margin-top:6px;display:flex;gap:6px;align-items:center}
.voice p::before{content:"";width:8px;height:8px;background:var(--navy);border-radius:50%}
.news{left:200px;top:1766px;width:590px}
.news-list{margin-top:6px}
.news-list li{display:flex;align-items:center;gap:14px;height:34px;border-bottom:1px dashed var(--line);font-size:12px}
.tag{width:76px;height:18px;border-radius:9px;background:var(--navy);color:var(--white);font-size:10px;display:flex;align-items:center;justify-content:center}
.date{color:var(--muted);font-size:11px;width:80px}
.btn-small{left:440px;top:1984px;width:110px;height:24px;border-radius:12px;background:var(--navy);color:var(--white);font-size:10px;display:flex;align-items:center;justify-content:center}

.sidebar{left:832px;top:1562px;width:168px}
.side-list li{font-size:11px;height:26px;display:flex;align-items:center;border-bottom:1px solid var(--line);padding-left:6px}
.banner{height:56px;margin-top:12px;display:flex;align-items:center;justify-content:center;color:var(--white);font-size:12px;font-weight:500}
.banner.estimate{background:var(--navy)}
.banner.recruit{background:var(--blue)}
.side-title{margin-top:16px}

/* footer */
.site-footer{left:0;top:2032px;width:1200px;height:368px;background:var(--navy-deep)}
.footer-map{left:200px;top:2066px;width:240px;height:130px;background:linear-gradient(135deg,#d8dbe0,#eef0f3)}
.footer-info{left:470px;top:2068px;color:var(--white)}
.footer-info h4{font-size:13px;font-weight:700;margin-bottom:10px}
.footer-info p{font-size:11px;line-height:2;color:#c9d0e0}
.footer-nav{left:864px;top:2066px}
.footer-nav li{font-size:11px;color:var(--white);line-height:2.2}
.copyright{left:0;top:2400px;width:1200px;height:52px;background:#0a1433;color:#9aa3b8;font-size:10px;display:flex;align-items:center;justify-content:center}
.to-top{left:1150px;top:2406px;width:32px;height:32px;background:#283660;display:flex;align-items:center;justify-content:center}
</style>
</head>
<body>

<header class="abs site-header"></header>
<div class="abs brand"><span class="brand-mark"></span><span class="brand-name">TOMASEI</span></div>
<div class="abs brand-sub">トマセイ株式会社</div>
<ul class="abs global-nav">
  <li>事業紹介</li><li>会社概要</li><li>採用情報</li><li>スタッフ</li><li>施工事例</li><li>ブログ</li><li>お問合せ</li>
</ul>
<div class="abs nav-estimate">Web見積りは<br>こちら</div>

<section class="abs hero" role="img" aria-label="鉄製品の製造現場の写真"></section>
<h1 class="abs hero-title">High quality × Quick delivery</h1>
<p class="abs hero-lead">クオリティの高い鉄製品を短納期でご提供いたします</p>

<div class="abs features">
  <div class="feature" role="img" aria-label="製品を扱う作業の写真を背景にした紹介パネル">「高品質・短納期」で<br>ご提供いただけるサービス
    <svg class="arrow" viewBox="0 0 30 30"><circle cx="15" cy="15" r="14" fill="none" stroke="#fff" stroke-width="1.5"/><path d="M13 10l5 5-5 5" fill="none" stroke="#fff" stroke-width="2"/></svg></div>
  <div class="feature" role="img" aria-label="相談の様子の写真を背景にした紹介パネル">なんでもご相談いただける<br>柔軟な体制
    <svg class="arrow" viewBox="0 0 30 30"><circle cx="15" cy="15" r="14" fill="none" stroke="#fff" stroke-width="1.5"/><path d="M13 10l5 5-5 5" fill="none" stroke="#fff" stroke-width="2"/></svg></div>
  <div class="feature" role="img" aria-label="オフィスの写真を背景にした紹介パネル">常にお客様目線で取り組み<br>成長し続ける姿勢
    <svg class="arrow" viewBox="0 0 30 30"><circle cx="15" cy="15" r="14" fill="none" stroke="#fff" stroke-width="1.5"/><path d="M13 10l5 5-5 5" fill="none" stroke="#fff" stroke-width="2"/></svg></div>
</div>

<div class="abs section-label" style="top:718px"><small>Works</small><h2>施工事例</h2></div>
<div class="abs works-grid">
  <div class="work" role="img" aria-label="鉄骨階段の施工写真" style="background:linear-gradient(135deg,#7f90a3,#d5dbe2)"></div>
  <div class="work" role="img" aria-label="店舗内装の施工写真" style="background:linear-gradient(135deg,#8f7a63,#c9b59a)"></div>
  <div class="work" role="img" aria-label="建物外観の施工写真" style="background:linear-gradient(135deg,#a3b3c3,#e8ecf0)"></div>
  <div class="work" role="img" aria-label="オフィス内装の施工写真" style="background:linear-gradient(135deg,#b2b8c0,#eef0f2)"></div>
  <div class="work" role="img" aria-label="ショールームの施工写真" style="background:linear-gradient(135deg,#98a3ae,#dfe4e9)"></div>
  <div class="work" role="img" aria-label="フロア内装の施工写真" style="background:linear-gradient(135deg,#6e6156,#a89684)"></div>
  <div class="work" role="img" aria-label="店舗照明の施工写真" style="background:linear-gradient(135deg,#3d2f25,#8a6a4c)"></div>
  <div class="work" role="img" aria-label="カフェ内装の施工写真" style="background:linear-gradient(135deg,#4a3a2e,#98785a)"></div>
</div>
<div class="abs btn-more">一覧を見る</div>

<section class="abs strength"></section>
<div class="abs strength-photo" role="img" aria-label="書類を前に打ち合わせをする手元の写真"></div>
<div class="abs strength-body">
  <h3>クオリティの高い鉄製品を短納期でご提供いたします</h3>
  <p>当社は金属加工を中心に、設計から製作、施工までを一貫して行っております。長年培った技術と経験を活かし、お客様のご要望に柔軟にお応えします。全国の協力会社とのネットワークにより、高品質な製品をスピーディーにお届けいたします。</p>
  <ul class="strength-points"><li>設計対応</li><li>短納期対応</li></ul>
</div>

<div class="abs voices">
  <h3 class="col-title">先輩社員の声</h3>
  <div class="voice-list">
    <div class="voice"><div class="voice-photo" role="img" aria-label="製造スタッフの写真" style="background:linear-gradient(135deg,#5d6b7c,#a7b3bf)"></div><p>製造部 入社3年目</p></div>
    <div class="voice"><div class="voice-photo" role="img" aria-label="設計スタッフの写真" style="background:linear-gradient(135deg,#7a8794,#c3ccd4)"></div><p>設計部 入社5年目</p></div>
    <div class="voice"><div class="voice-photo" role="img" aria-label="営業スタッフの写真" style="background:linear-gradient(135deg,#3b4452,#8d97a4)"></div><p>営業部 入社2年目</p></div>
  </div>
</div>

<div class="abs news">
  <h3 class="col-title">新着情報・スタッフブログ</h3>
  <ul class="news-list">
    <li><span class="tag">新着情報</span><span class="date">2024.10.12</span>施工事例を更新しました</li>
    <li><span class="tag">ブログ</span><span class="date">2024.10.08</span>現場研修について</li>
    <li><span class="tag">新着情報</span><span class="date">2024.09.30</span>夏季休業のお知らせ</li>
    <li><span class="tag">ブログ</span><span class="date">2024.09.21</span>新しい設備を導入しました</li>
    <li><span class="tag">新着情報</span><span class="date">2024.09.10</span>採用情報を更新しました</li>
  </ul>
</div>
<div class="abs btn-small">一覧を見る</div>

<aside class="abs sidebar">
  <h3 class="col-title">新着紹介</h3>
  <ul class="side-list"><li>グローバルサイト</li><li>会社概要</li><li>施工事例</li></ul>
  <div class="banner estimate">Web見積りはこちら</div>
  <div class="banner recruit">採用情報</div>
  <h3 class="col-title side-title">コンテンツ</h3>
  <ul class="side-list"><li>事業紹介</li><li>会社概要</li><li>スタッフブログ</li><li>施工事例</li><li>採用情報</li><li>ブログ</li></ul>
</aside>

<footer class="abs site-footer"></footer>
<div class="abs footer-map" role="img" aria-label="会社所在地の地図"></div>
<div class="abs footer-info">
  <h4>会社名が入ります会社名が入ります</h4>
  <p>〒000-0000<br>住所が入ります住所が入ります<br>TEL 00-0000-0000</p>
</div>
<ul class="abs footer-nav">
  <li>事業紹介</li><li>会社概要</li><li>採用情報</li><li>スタッフブログ</li><li>施工事例</li><li>ブログ</li><li>お問合せ</li>
</ul>
<div class="abs copyright">Copyright © TOMASEI All Rights Reserved.</div>
<div class="abs to-top"><svg width="14" height="10" viewBox="0 0 14 10"><path d="M2 8l5-5 5 5" fill="none" stroke="#fff" stroke-width="2"/></svg></div>

</body>
</html>
```